Business card design for Summit Wallcrafters required

Our company "Boardline Finishing Harbor Works" needs business cards. Make the business cards be found easily amongst 100 other construction business cards. White background, logo centered and large.

Target Market(s)

Customers or builders who need a drywaller and customers who need a very high quality drywaller.

Industry/Entity Type

Construction

Contact Information for Business Card

The business logo centered and large with "Serving Ridgewater County 15+years" in black Italic, and 2 telephone numbers centered beneath written: Ada / Lou: 403-682-1357, and 403-739-2864 beneath. The business cards will be printed in metal with rounded corners.

Colors
ec1f27

Requirements
Must have
• The selected logo. Must be able to see "DRYWALL" from a distance. Must stick out from other business cards.

```html
<!DOCTYPE html>
<html lang="en">
<head>
<meta charset="utf-8">
<title>Boardline Finishing Harbor Works – Business Card</title>
<link href="https://fonts.googleapis.com/css2?family=Lato:ital,wght@0,300;0,400;0,700;0,900;1,700&display=swap" rel="stylesheet">
<style>
  :root {
    --backdrop: #2a2a2a;
    --card-white: #f4f4f4;
    --brand-red: #ec1f27;
    --brand-red-dark: #c8161d;
    --ink: #3a3a3a;
    --on-red: #ffffff;
  }
  html, body {
    margin: 0;
    padding: 0;
    width: 1200px;
    height: 873px;
    overflow: hidden;
    background: var(--backdrop);
    font-family: "Lato", sans-serif;
  }
  .stage {
    width: 1200px;
    height: 873px;
    display: flex;
    align-items: center;
    justify-content: center;
  }
  .business-card {
    position: relative;
    width: 760px;
    height: 434px;
    background: linear-gradient(180deg, #fbfbfb 0%, var(--card-white) 100%);
    border-radius: 22px;
    overflow: hidden;
    box-shadow: 0 18px 40px rgba(0,0,0,0.45);
  }
  .brand {
    position: absolute;
    top: 72px;
    left: 0;
    right: 0;
    display: flex;
    align-items: center;
    justify-content: center;
    gap: 16px;
  }
  .brand-square {
    width: 54px;
    height: 54px;
    background: var(--brand-red);
    flex: none;
  }
  .brand-name {
    font-weight: 900;
    font-size: 36px;
    color: var(--brand-red);
    letter-spacing: 0.2px;
    line-height: 1;
  }
  .contact-band {
    position: absolute;
    top: 180px;
    left: 0;
    width: 100%;
    height: 92px;
    background: linear-gradient(90deg, var(--brand-red) 0%, var(--brand-red-dark) 100%);
  }
  .contact-band .divider {
    position: absolute;
    left: 0;
    top: 0;
  }
  .contact {
    position: absolute;
    top: 16px;
    width: 50%;
    text-align: center;
    color: var(--on-red);
  }
  .contact-left { left: 0; }
  .contact-right { right: 0; }
  .contact-name {
    font-weight: 700;
    font-size: 21px;
    line-height: 1.2;
  }
  .contact-phone {
    font-weight: 300;
    font-size: 27px;
    letter-spacing: 0.5px;
    line-height: 1.3;
  }
  .tagline {
    position: absolute;
    top: 338px;
    left: 0;
    right: 0;
    margin: 0;
    text-align: center;
    font-weight: 700;
    font-size: 19px;
    color: var(--ink);
  }
</style>
</head>
<body>
  <main class="stage">
    <article class="business-card">
      <header class="brand">
        <span class="brand-square" aria-hidden="true"></span>
        <span class="brand-name">Boardline Finishing Harbor Works</span>
      </header>

      <section class="contact-band">
        <svg class="divider" width="760" height="92" viewBox="0 0 760 92" aria-hidden="true">
          <line x1="392" y1="4" x2="368" y2="88" stroke="#ffffff" stroke-opacity="0.75" stroke-width="2"/>
        </svg>
        <div class="contact contact-left">
          <div class="contact-name">Ada:</div>
          <div class="contact-phone">403-682-1357</div>
        </div>
        <div class="contact contact-right">
          <div class="contact-name">Lou:</div>
          <div class="contact-phone">403-739-2864</div>
        </div>
      </section>

      <p class="tagline">Serving Ridgewater County 15+years</p>
    </article>
  </main>
</body>
</html>
```